Poetry Book Cover Design Project

Looking for a minimalistic book cover design for a collection of poems. The book title is "Before The Morning Turns To Glass". There are three parts to the book. First covers poetry in the theme of Rage. Second love and desire. The third is strange poems. Essentially the sections are "Rage", "Desire" and the "Strange". The reason for the title "Before The Morning Turns To Glass" is as if someone is writing these till life changes towards the intended outcome as felt in each poem. I want to have the author's name "Nirosha Kulathunge" at the bottom. Ilustration attached.
- Minimalistic

```html
<!DOCTYPE html>
<html lang="en">
<head>
<meta charset="utf-8">
<title>Before The Morning Turns To Glass — Cover Editions</title>
<link href="https://fonts.googleapis.com/css2?family=EB+Garamond:wght@400;500&display=swap" rel="stylesheet">
<style>
  :root {
    --page: #ffffff;
    --ink: #1a1a1a;
    --night: #231f20;
    --paper: #ffffff;
    --grey-light: #d4d4d4;
    --grey-mid: #9a9a9a;
    --grey-dark: #555555;
  }
  * { margin: 0; padding: 0; box-sizing: border-box; }
  html, body {
    width: 1200px;
    height: 1200px;
    overflow: hidden;
    background: var(--page);
  }
  .stage {
    position: relative;
    width: 1200px;
    height: 1200px;
  }
  .cover {
    position: absolute;
    width: 400px;
    height: 580px;
    font-family: "EB Garamond", Georgia, serif;
    overflow: hidden;
  }
  .cover--night {
    left: 170px;
    top: 540px;
    background: var(--night);
    color: var(--paper);
  }
  .cover--day {
    left: 640px;
    top: 130px;
    background: var(--paper);
    color: var(--ink);
    box-shadow: 0 0 0 1px #e6e6e6;
  }
  .cover__art {
    position: absolute;
    inset: 0;
    width: 100%;
    height: 100%;
  }
  .cover__title {
    position: absolute;
    top: 52px;
    right: 34px;
    text-align: right;
    font-weight: 400;
    font-size: 50px;
    line-height: 1.04;
    letter-spacing: 0.01em;
  }
  .cover__title span { display: block; }
  .cover__author {
    position: absolute;
    left: 108px;
    bottom: 48px;
    font-size: 15px;
    letter-spacing: 0.03em;
  }
</style>
</head>
<body>
<main class="stage">

  <article class="cover cover--night">
    <svg class="cover__art" viewBox="0 0 400 580" role="img" aria-label="Line illustration of a rose with flowing ribbons sweeping down the left side and across the lower cover">
      <defs>
        <linearGradient id="ribbon-night" x1="0" y1="0" x2="1" y2="1">
          <stop offset="0" stop-color="var(--grey-mid)" stop-opacity="0.45"/>
          <stop offset="1" stop-color="var(--grey-light)" stop-opacity="0.25"/>
        </linearGradient>
      </defs>
      <path d="M70 0 C120 80 60 160 110 240 C140 300 80 340 90 380 C160 400 260 380 400 350 L400 420 C300 440 200 470 110 470 C60 500 40 540 40 580 L0 580 L0 0 Z" fill="url(#ribbon-night)"/>
    </svg>
    <h1 class="cover__title">
      <span>Before</span><span>The</span><span>Morning</span><span>Turns</span><span>To</span><span>Glass</span>
    </h1>
    <p class="cover__author">Nirosha Kulathunge</p>
  </article>

  <article class="cover cover--day">
    <svg class="cover__art" viewBox="0 0 400 580" role="img" aria-label="Line illustration of a rose with flowing ribbons sweeping down the left side and across the lower cover">
      <defs>
        <linearGradient id="ribbon-day" x1="0" y1="0" x2="1" y2="1">
          <stop offset="0" stop-color="var(--grey-mid)" stop-opacity="0.35"/>
          <stop offset="1" stop-color="var(--grey-dark)" stop-opacity="0.2"/>
        </linearGradient>
      </defs>
      <path d="M70 0 C120 80 60 160 110 240 C140 300 80 340 90 380 C160 400 260 380 400 350 L400 420 C300 440 200 470 110 470 C60 500 40 540 40 580 L0 580 L0 0 Z" fill="url(#ribbon-day)"/>
    </svg>
    <h1 class="cover__title">
      <span>Before</span><span>The</span><span>Morning</span><span>Turns</span><span>To</span><span>Glass</span>
    </h1>
    <p class="cover__author">Nirosha Kulathunge</p>
  </article>

</main>
</body>
</html>
```